Business Card Design Project

Branding and Marketing Company

Target Market(s)

Lifestyle Brands. Velorra, Quince, Brisk Harbor

Industry/Entity Type

Business

Contact Information for Business Card

I'm looking for a sleek design that is simple yet stands out. I would like to see some embossed options and even metallic features. I am looking for a black and white theme business card. Our company font is Avenir (Regular, Italic, Bold) I would like to have just the logo and the following slogan on the back of card.CREATING THE NEXT BIG THING IN HEALTH & WELLNESS

```html
<!DOCTYPE html>
<html lang="en">
<head>
<meta charset="utf-8">
<title>Lumo Crest – Business Card</title>
<link rel="stylesheet" href="https://fonts.googleapis.com/css2?family=Nunito+Sans:wght@400;700;800&display=swap">
<style>
  :root {
    --stage: #2b2b2b;
    --card: #f4f4f4;
    --card-edge: #dcdcdc;
    --ink: #1a1a1a;
    --ink-soft: #444444;
  }
  * { margin: 0; padding: 0; box-sizing: border-box; }
  html, body {
    width: 1200px; height: 997px; overflow: hidden;
    background: var(--stage);
    font-family: "Nunito Sans", "Avenir", sans-serif;
    color: var(--ink);
  }
  .stage {
    width: 1200px; height: 997px;
    display: flex; align-items: center; justify-content: center; gap: 40px;
  }
  .card {
    position: relative;
    width: 530px; height: 303px;
    border-radius: 16px;
    background: linear-gradient(160deg, #ffffff 0%, var(--card) 60%, var(--card-edge) 100%);
    overflow: hidden;
  }

  /* Front */
  .front-logo {
    position: absolute; left: 0; right: 0; top: 96px;
    display: flex; align-items: center; justify-content: center; gap: 14px;
  }
  .brand-mark {
    width: 30px; height: 30px; border-radius: 50%; background: var(--ink);
  }
  .brand-name {
    font-weight: 700; font-size: 40px; letter-spacing: 1px; color: var(--ink);
    line-height: 1;
  }
  .slogan {
    position: absolute; left: 0; right: 0; bottom: 34px;
    text-align: center; font-size: 12.5px; letter-spacing: 1.2px;
    color: var(--ink-soft);
  }

  /* Back */
  .back-logo {
    position: absolute; right: 40px; top: 30px;
    display: flex; align-items: center; gap: 10px;
  }
  .back-logo .brand-mark { width: 20px; height: 20px; }
  .back-logo .brand-name { font-size: 24px; }
  .rule-top {
    position: absolute; left: 210px; right: 34px; top: 110px;
    height: 2px; background: var(--ink);
  }
  .person {
    position: absolute; left: 34px; top: 142px; right: 34px;
  }
  .person-name-row { display: flex; align-items: flex-end; gap: 8px; }
  .person-name { font-weight: 800; font-size: 19px; line-height: 1; white-space: nowrap; }
  .person-rule { flex: 1; height: 2px; background: var(--ink); margin-bottom: 2px; }
  .person-title {
    font-weight: 700; font-size: 10.5px; letter-spacing: 0.5px; margin-top: 4px;
  }
  .web {
    position: absolute; right: 34px; top: 172px;
    font-weight: 700; font-size: 13px; letter-spacing: 1.4px;
  }
  .contacts {
    position: absolute; left: 34px; top: 202px; list-style: none;
  }
  .contacts li {
    display: flex; align-items: center; gap: 10px;
    font-size: 13.5px; color: var(--ink-soft); height: 21px;
  }
  .contacts svg { width: 15px; height: 15px; flex: none; }
</style>
</head>
<body>
<main class="stage">
  <section class="card card-front" aria-label="Card front">
    <div class="front-logo">
      <span class="brand-mark"></span>
      <span class="brand-name">lumo crest</span>
    </div>
    <p class="slogan">CREATING THE NEXT BIG THING IN HEALTH &amp; WELLNESS</p>
  </section>

  <section class="card card-back" aria-label="Card back">
    <div class="back-logo">
      <span class="brand-mark"></span>
      <span class="brand-name">lumo crest</span>
    </div>
    <div class="rule-top"></div>
    <div class="person">
      <div class="person-name-row">
        <span class="person-name">Maren Holloway</span>
        <span class="person-rule"></span>
      </div>
      <p class="person-title">FOUNDER &amp; CEO</p>
    </div>
    <p class="web">www.lumocrest.com</p>
    <ul class="contacts">
      <li>
        <svg viewBox="0 0 16 16"><circle cx="8" cy="8" r="8" fill="#1a1a1a"/><path d="M5 5.5 L6.5 4.5 L7.5 6.5 L6.8 7.2 Q7.8 9 9 9.2 L9.6 8.5 L11.5 9.5 L10.5 11 Q6 10.5 5 5.5Z" fill="#fff"/></svg>
        0412 555 018
      </li>
      <li>
        <svg viewBox="0 0 16 16"><circle cx="8" cy="8" r="8" fill="#1a1a1a"/><rect x="5.8" y="3.8" width="4.4" height="8.4" rx="0.8" fill="#fff"/><rect x="6.5" y="5" width="3" height="5" fill="#1a1a1a"/></svg>
        0398 555 274
      </li>
      <li>
        <svg viewBox="0 0 16 16"><circle cx="8" cy="8" r="8" fill="#1a1a1a"/><rect x="4" y="5.2" width="8" height="5.6" fill="#fff"/><path d="M4 5.2 L8 8.5 L12 5.2" stroke="#1a1a1a" stroke-width="0.9" fill="none"/></svg>
        hello@lumocrest.com.au
      </li>
      <li>
        <svg viewBox="0 0 16 16"><circle cx="8" cy="8" r="8" fill="#1a1a1a"/><path d="M8 3.8 L12.2 7.6 H11 V11.8 H9 V9.2 H7 V11.8 H5 V7.6 H3.8Z" fill="#fff"/></svg>
        Suite 4B, 112 Alder Road, Perth
      </li>
    </ul>
  </section>
</main>
</body>
</html>
```